new letterhead/envelope/business card design for law firm

please see attached pdf of current letterhead, envelope and business card. I am also attaching my new logo that I would like to be used. basically, I am looking to refresh and simplify my letterhead/stationary and business card, keeping the following in mind:

overall, I am going for the following look:

-simple,
-modern,
-classy,
-professional

Target Market(s)

law firm clients

Industry/Entity Type

Law Firm

Contact Information for Business Card

see attachment

Font styles to use
Sans Serif

Requirements
Must have
• overall, I am going for the following look:
• -simple,
• -modern,
• -classy,
• -professional
Nice to have
• same as above
Should not have
• no serif fonts

```html
<!DOCTYPE html>
<html lang="en">
<head>
<meta charset="utf-8">
<title>Hollis Law – Letterhead</title>
<link rel="stylesheet" href="https://fonts.googleapis.com/css2?family=Montserrat:wght@400;500;600;700&display=swap">
<style>
  :root {
    --backdrop: #eceeed;
    --paper: #ffffff;
    --navy: #0f2f55;
    --green: #4f9a3a;
    --ink: #2a2a2a;
    --signature: #2a3fd0;
  }
  * { box-sizing: border-box; margin: 0; padding: 0; }
  html, body {
    width: 1200px; height: 1200px; overflow: hidden;
    background: var(--backdrop);
    font-family: "Montserrat", Arial, sans-serif;
  }
  .sheet {
    position: absolute;
    left: 237px; top: 85px;
    width: 727px; height: 1028px;
    background: var(--paper);
  }
  .brand {
    position: absolute;
    left: 70px; top: 79px;
    display: flex; align-items: center; gap: 14px;
  }
  .brand-mark {
    width: 60px; height: 60px; border-radius: 50%;
    background: var(--navy);
  }
  .brand-name {
    font-weight: 700; font-size: 33px; letter-spacing: 0.5px;
    color: var(--navy);
  }
  .contact {
    position: absolute;
    right: 63px; top: 64px;
    text-align: right;
    color: var(--navy);
    font-size: 13px; font-weight: 500; line-height: 17px;
  }
  .contact .address { margin-bottom: 4px; }
  .contact .line { display: flex; justify-content: flex-end; align-items: center; gap: 5px; }
  .contact svg { width: 10px; height: 10px; fill: none; stroke: var(--green); stroke-width: 1.6; }
  .letter-body {
    position: absolute;
    left: 104px; top: 342px;
    width: 520px;
    font-size: 12.4px; line-height: 14.3px;
    color: var(--ink);
    text-align: justify;
  }
  .letter-body p + p { margin-top: 14.3px; }
  .signature {
    position: absolute;
    left: 92px; top: 760px;
    width: 186px; height: 40px;
    background: linear-gradient(90deg, rgba(42,63,208,0.14), rgba(42,63,208,0.04));
    border-radius: 4px;
  }
  .signer-title {
    position: absolute;
    left: 104px; top: 805px;
    font-size: 13.5px; color: var(--ink);
  }
</style>
</head>
<body>
  <main class="sheet">
    <header>
      <div class="brand">
        <div class="brand-mark"></div>
        <div class="brand-name">HOLLIS LAW</div>
      </div>
      <address class="contact" style="font-style:normal">
        <div class="address">2240 Larkfield Avenue, Suite 410<br>Durham, NC 27705</div>
        <div class="line">919 555 0142
          <svg viewBox="0 0 10 10" aria-label="phone"><path d="M1.5 3.5 Q5 0.5 8.5 3.5 L7.5 5 L6 4 L4 4 L2.5 5 Z M2.5 6 H7.5 V8.5 H2.5 Z"/></svg>
        </div>
        <div class="line">919 555 0187
          <svg viewBox="0 0 10 10" aria-label="fax"><path d="M3 1.2 H7 V3.5 M1.2 3.5 H8.8 V7 H1.2 Z M3 6 H7 V8.8 H3 Z"/></svg>
        </div>
        <div class="line">www.hollislawpa.com
          <svg viewBox="0 0 10 10" aria-label="website"><circle cx="5" cy="5" r="3.9"/><path d="M1.1 5 H8.9 M5 1.1 Q2.5 5 5 8.9 M5 1.1 Q7.5 5 5 8.9"/></svg>
        </div>
      </address>
    </header>

    <section class="letter-body">
      <p>Letterhead samples are a great way of deciding what kind of letterhead you want to design for you and your company. The internet has a ton of great letterhead samples to browse through. Whether you want something simple, with just a couple lines of text of your business information, or something decorative and stunning, with photos and logos on the top and bottom of the page, it will be easy to find what you want, because there are samples online for basically any type of letterhead you could want.</p>
      <p>Any business could easily benefit from browsing through some letterhead samples, if only to get an idea for what kind of letterhead their company might want. Letterheads are just one of the tools that a business professional could use to help increase their customer base, and to really be memorable to everyone they write a letter to. Letterhead is quite an effective tool for marketing and advertising, but because it’s such a simple and well known idea, it is often unfairly overlooked. Make sure you don’t make that mistake, and make some letterhead samples of your own today.</p>
      <p>Whether you want to get new customers to remember you and become part of your clientele, or you just want to send out friendly reminders to your existing clients, customizing your own letterhead samples can really help you out. Try out some letterhead samples and you will not regret it, and I’m sure you will add a new tool to your business’ arsenal of networking, marketing, and advertising tools.</p>
    </section>

    <div class="signature" role="img" aria-label="Handwritten signature of Daniel Marsh"></div>
    <div class="signer-title">company director</div>
  </main>
</body>
</html>
```